New shirt company looking for a fun and edgy online retail website design

We're a new company looking for a simple yet attractive website to sell shirts/tops to a mostly younger female audience. Our name is Tavi Shirt Co. and the PlanHerd logo is uploaded. We're thinking a home page, three separate pages for our shirt "collections", and a contact page/cart page for a grand total of 5 pages. We'd like the website to be coded, easy for the consumer to navigate/shop/checkout, and easy to link to various social media platforms and online websites. For colors, we're aiming for various blues, light grey, and maybe tan/khaki. Our goal is to launch with approximately 20-30 tops/shirts (or 7-10) per page. Please let us know if you have any questions and thank you for helping us! We are very excited to see what is created!

Target Market(s)

Female teens to early twenties

Coding

Coded - Design and coding required

Number of Pages Required

3 page

Font styles to use
Decorative
Script

Colors
cee9f5
85cae6
33a6d7
0393ce
cfdfed
85acd3

Requirements
Must have
• Online shopping/purchasing capabilities, dropdowns to select sizes for each item, easy to add/remove new or seasoned items.

```html
<!DOCTYPE html>
<html lang="en">
<head>
<meta charset="utf-8">
<title>Tavi Shirt Co. — Collections</title>
<link rel="stylesheet" href="https://fonts.googleapis.com/css2?family=Great+Vibes&family=Poppins:wght@400;500;600;700&family=Roboto:wght@400;500&display=swap">
<style>
:root{
  --sky:#85cae6;
  --ocean:#0393ce;
  --navy:#0d3c6e;
  --pill:#e6f2fa;
  --ink:#222;
  --muted:#666;
  --border:#d9d9d9;
  --star:#f5a623;
  --footer:#20242b;
  --footer-dark:#17191e;
  --footer-text:#c9ccd2;
}
*{margin:0;padding:0;box-sizing:border-box}
html,body{width:1200px;height:2672px;overflow:hidden;background:#fff}
body{position:relative;font-family:'Poppins',sans-serif;color:var(--ink)}
.abs{position:absolute}

/* hero */
.hero{left:0;top:0;width:1200px;height:395px;background:linear-gradient(90deg,var(--sky) 0 600px,var(--ocean) 600px 1200px)}
.hero-photo{left:809px;top:26px;width:275px;height:369px;background:linear-gradient(180deg,#7a4a36 0%,#e7d4bf 30%,#f4efdc 60%,#efe8d3 100%);border-radius:120px 120px 0 0}
.brand{left:117px;top:29px;width:173px;height:70px;border:2px solid var(--navy);display:flex;flex-direction:column;align-items:center;justify-content:center;gap:2px;color:var(--navy)}
.brand .name{font-family:'Poppins',sans-serif;font-weight:600;font-size:26px;line-height:1}
.brand .sub{font-family:'Poppins',sans-serif;font-weight:600;font-size:11px;letter-spacing:1.5px}
.nav{left:381px;top:41px;width:588px;height:44px;display:flex;border-radius:22px;overflow:hidden;font-family:'Roboto',sans-serif;font-size:17px}
.nav .links{flex:0 0 428px;background:var(--pill);display:flex;align-items:center;gap:31px;padding-left:36px}
.nav .links .active{color:var(--ocean)}
.nav .cta{flex:1;background:var(--navy);color:#fff;display:flex;align-items:center;padding-left:37px}
.cart{left:1050px;top:50px}
.cart-badge{left:1066px;top:42px;width:16px;height:16px;border-radius:50%;background:#e0161c;color:#fff;font-size:10px;text-align:center;line-height:16px;font-family:'Roboto',sans-serif}
.hero-title{left:0;width:1200px;top:195px;text-align:center;font-family:'Great Vibes',cursive;font-size:74px;font-weight:400;color:#fff}
.crumb{left:0;width:1200px;top:297px;text-align:center;font-family:'Roboto',sans-serif;font-size:15px;color:#fff}
.crumb span{margin:0 13px}

/* shop */
.section-title{left:0;width:1200px;top:462px;text-align:center;font-size:30px;font-weight:400;color:var(--ocean)}
.filters{left:122px;top:522px;display:flex;align-items:center;font-size:15px;font-weight:500}
.filters .label{font-weight:400;color:#444;margin-right:26px}
.filters .item{margin-right:28px;display:flex;align-items:center;gap:4px}
.filters .caret{font-size:10px;color:#999}
.sorting{left:801px;top:525px;font-size:13px;color:#555}
.views{left:990px;top:524px;display:flex;gap:9px}
.views i{display:block;width:15px;height:15px;background:repeating-linear-gradient(90deg,#999 0 2px,#fff 2px 3px)}
.views i.on{background:repeating-linear-gradient(90deg,#555 0 2px,#fff 2px 4px)}
.views i.list{background:repeating-linear-gradient(180deg,#999 0 2px,#fff 2px 4px)}

.card{width:221px;height:346px;border:1px solid var(--border);background:#fff}
.card.hover{border:2px solid var(--ocean);box-shadow:0 10px 18px rgba(0,0,0,.12)}
.card .photo{height:246px;border-bottom:1px solid var(--border)}
.card .title{margin:12px 0 0 22px;font-family:'Great Vibes',cursive;font-size:26px;line-height:30px}
.card .title.plain{font-family:'Poppins',sans-serif;font-size:16px;font-weight:500;margin-top:16px;line-height:24px}
.card .stars{margin-left:22px;color:var(--star);font-size:13px;letter-spacing:1px;line-height:18px}
.card .price{margin:6px 0 0 22px;font-size:17px;font-weight:600}
.actions{display:flex;flex-direction:column;gap:14px;position:absolute;right:14px;top:116px}
.actions span{width:40px;height:40px;border-radius:50%;border:2px solid var(--navy);background:#fff;display:flex;align-items:center;justify-content:center}
.actions span.fill{background:var(--ocean);border-color:var(--ocean)}

.pager{left:470px;top:1743px;display:flex;gap:10px}
.pager span{width:35px;height:35px;border-radius:50%;border:2px solid #9fd0e8;color:#9fb7c4;display:flex;align-items:center;justify-content:center;font-size:15px}
.pager span.on{background:var(--ocean);border-color:var(--ocean);color:#fff}
.pager span.arrow{color:var(--navy);font-size:20px}

/* social feed */
.feed-title{left:273px;top:1872px;font-size:29px;font-weight:700;color:#333}
.feed-text{left:273px;top:1916px;width:640px;font-size:16px;line-height:21px;color:#333}
.shot{position:absolute}

/* footer */
.footer{left:0;top:2379px;width:1200px;height:215px;background:var(--footer)}
.footer-bottom{left:0;top:2594px;width:1200px;height:78px;background:var(--footer-dark)}
.f-policy{left:118px;top:2425px;font-family:'Roboto',sans-serif;font-size:13px;line-height:27px;color:#fff}
.f-rule{left:118px;top:2487px;width:190px;height:1px;background:#3a3f48}
.f-contact{left:118px;top:2502px;font-family:'Roboto',sans-serif;font-size:13px;line-height:24px;color:var(--footer-text)}
.f-div{width:1px;height:145px;background:#353a42;top:2425px}
.f-head{font-family:'Roboto',sans-serif;font-size:16px;color:#fff}
.f-links{left:461px;top:2426px;font-family:'Roboto',sans-serif}
.f-links ul{list-style:none;margin-top:15px;font-size:14px;line-height:23px;color:var(--footer-text)}
.f-links li:first-child{color:#fff}
.f-news{left:727px;top:2424px;font-family:'Roboto',sans-serif}
.f-news p{font-size:13.5px;margin-top:12px;color:var(--footer-text)}
.subscribe{left:719px;top:2490px;width:364px;height:38px;display:flex;border-radius:19px;overflow:hidden}
.subscribe .field{flex:1;background:#fff;color:#888;font-family:'Roboto',sans-serif;font-size:13px;padding-left:26px;display:flex;align-items:center}
.subscribe .btn{width:118px;background:var(--ocean);color:#fff;font-weight:500;font-family:'Poppins',sans-serif;font-size:14px;display:flex;align-items:center;justify-content:center}
.socials{left:723px;top:2535px;width:157px;height:35px;background:#2a2e36;display:flex;align-items:center;gap:14px;padding-left:10px}
.socials i{width:14px;height:14px;border-radius:50%;background:#9aa0a8;display:block}
.copy{left:120px;top:2623px;font-family:'Roboto',sans-serif;font-size:13.5px;color:#9aa0a8}
.cards{left:738px;top:2617px;display:flex;gap:11px}
.cards i{display:block;width:49px;height:30px;border-radius:3px;background:#fff}
.cards i::after{content:"";display:block;width:25px;height:10px;margin:10px auto;border-radius:2px;background:#c9d3df}
</style>
</head>
<body>

<header>
  <div class="abs hero"></div>
  <div class="abs hero-photo" role="img" aria-label="Photo of a young woman wearing a cream t-shirt"></div>
  <div class="abs brand"><span class="name">Tavi</span><span class="sub">SHIRT CO.</span></div>
  <nav class="abs nav">
    <div class="links"><span>Home</span><span>Our Shirt</span><span class="active">Collections</span><span>Contact</span></div>
    <div class="cta">Shop Now</div>
  </nav>
  <svg class="abs cart" width="24" height="22" viewBox="0 0 24 22" fill="none" stroke="#fff" stroke-width="2" stroke-linejoin="round"><path d="M1 2h4l3 12h12l3-9H6"/><circle cx="9" cy="19" r="1.6" fill="#fff"/><circle cx="19" cy="19" r="1.6" fill="#fff"/></svg>
  <div class="abs cart-badge">0</div>
  <h1 class="abs hero-title">Collections</h1>
  <div class="abs crumb">Home<span>|</span>Collections</div>
</header>

<main>
  <h2 class="abs section-title">New Arrival</h2>
  <div class="abs filters">
    <span class="label">Filter by:</span>
    <span class="item"><svg width="16" height="18" viewBox="0 0 16 18" fill="none" stroke="#999"><rect x="1.5" y="2.5" width="13" height="15"/><path d="M4 7h8M4 10h8M4 13h6"/></svg>&nbsp;Categories</span>
    <span class="item">Colors <span class="caret">&#8964;</span></span>
    <span class="item">Sizes <span class="caret">&#8964;</span></span>
    <span class="item">Price <span class="caret">&#8964;</span></span>
  </div>
  <div class="abs sorting">Default sorting</div>
  <div class="abs views"><i></i><i class="on"></i><i style="width:9px"></i><i class="list"></i></div>

  <!-- row 1 -->
  <article class="abs card" style="left:119px;top:574px"><div class="photo" role="img" aria-label="Woman in red striped blouse" style="background:linear-gradient(#8d8d90,#c9c3c4 50%,#cfa3a8)"></div><div class="title">Product Name</div><div class="stars">★★★★☆</div><div class="price">$120.00</div></article>
  <article class="abs card hover" style="left:367px;top:574px"><div class="photo" role="img" aria-label="Woman in beige button-up shirt" style="background:linear-gradient(#bdbdc0,#e8dcc4 55%,#d8c7a4)"></div><div class="title">Product Name</div><div class="stars">★★★☆☆</div><div class="price">$120.00</div>
    <div class="actions">
      <span><svg width="16" height="16" viewBox="0 0 16 16" fill="none" stroke="#0d3c6e" stroke-width="1.6"><path d="M2 6V2h4M14 6V2h-4M2 10v4h4M14 10v4h-4M3 3l10 10M13 3L3 13"/></svg></span>
      <span><svg width="17" height="15" viewBox="0 0 17 15" fill="none" stroke="#0d3c6e" stroke-width="1.5"><path d="M8.5 14S1 9.5 1 4.8A3.6 3.6 0 0 1 8.5 3a3.6 3.6 0 0 1 7.5 1.8C16 9.5 8.5 14 8.5 14z"/></svg></span>
      <span class="fill"><svg width="20" height="18" viewBox="0 0 24 22" fill="none" stroke="#fff" stroke-width="2"><path d="M1 2h4l3 12h12l3-9H6"/><circle cx="9" cy="19" r="1.5"/><circle cx="19" cy="19" r="1.5"/></svg></span>
    </div>
  </article>
  <article class="abs card" style="left:615px;top:574px"><div class="photo" role="img" aria-label="Girl in white printed top" style="background:linear-gradient(#f4f4f4,#eceef2 60%,#c9d6e6)"></div><div class="title">Product Name</div><div class="stars">★★★★☆</div><div class="price" style="margin-top:26px">$120.00</div></article>
  <article class="abs card" style="left:863px;top:574px"><div class="photo" role="img" aria-label="Woman in floral white blouse" style="background:linear-gradient(#b8b8bb,#efe6e6 55%,#e6d3d5)"></div><div class="title">Product Name</div><div class="stars">★★★☆☆</div><div class="price" style="margin-top:26px">$120.00</div></article>

  <!-- row 2 -->
  <article class="abs card" style="left:119px;top:957px"><div class="photo" role="img" aria-label="Girl in light blue ruffle top" style="background:linear-gradient(#f4f4f4,#cfe0ee 55%,#b6cde2)"></div><div class="title plain">Product Name</div><div class="stars">★★★★☆</div><div class="price">$120.00</div></article>
  <article class="abs card" style="left:367px;top:957px"><div class="photo" role="img" aria-label="Woman in dotted floral blouse" style="background:linear-gradient(#b5b5b8,#efe9e6 55%,#e2d6d2)"></div><div class="title">Product Name</div><div class="stars">★★★★☆</div><div class="price">$120.00</div></article>
  <article class="abs card" style="left:615px;top:957px"><div class="photo" role="img" aria-label="Woman in maroon striped top" style="background:linear-gradient(#d8d8da,#a8757c 55%,#6e2a35)"></div><div class="title">Product Name</div><div class="stars">★★★★☆</div><div class="price">$120.00</div></article>
  <article class="abs card" style="left:863px;top:957px"><div class="photo" role="img" aria-label="Woman in checked shirt" style="background:linear-gradient(#8f8f93,#d4cccc 55%,#6d2f37)"></div><div class="title">Product Name</div><div class="stars">★★★☆☆</div><div class="price">$120.00</div></article>

  <!-- row 3 -->
  <article class="abs card" style="left:119px;top:1331px"><div class="photo" role="img" aria-label="Woman in red striped blouse" style="background:linear-gradient(#8d8d90,#c9c3c4 50%,#cfa3a8)"></div><div class="title">Product Name</div><div class="stars">★★★★☆</div><div class="price">$120.00</div></article>
  <article class="abs card" style="left:367px;top:1331px"><div class="photo" role="img" aria-label="Woman in beige button-up shirt" style="background:linear-gradient(#bdbdc0,#e8dcc4 55%,#d8c7a4)"></div><div class="title">Product Name</div><div class="stars">★★★☆☆</div><div class="price">$120.00</div></article>
  <article class="abs card" style="left:615px;top:1331px"><div class="photo" role="img" aria-label="Girl in white printed top" style="background:linear-gradient(#f4f4f4,#eceef2 60%,#c9d6e6)"></div><div class="title">Product Name</div><div class="stars">★★★★☆</div><div class="price">$120.00</div></article>
  <article class="abs card" style="left:863px;top:1331px"><div class="photo" role="img" aria-label="Woman in floral white blouse" style="background:linear-gradient(#b8b8bb,#efe6e6 55%,#e6d3d5)"></div><div class="title">Product Name</div><div class="stars">★★★☆☆</div><div class="price">$120.00</div></article>

  <div class="abs pager"><span class="arrow">&#8249;</span><span>1</span><span class="on">2</span><span>3</span><span>4</span><span class="arrow">&#8250;</span></div>

  <section>
    <h2 class="abs feed-title">Pixgram</h2>
    <p class="abs feed-text">Meet your fellow Tavi! Show us your TSC style on Chirper, Pixgram or Facenote and tag @ Tavi for a chance to win free tees and be featured on our site!</p>
    <div class="shot" role="img" aria-label="Woman in navy blouse against concrete wall" style="left:255px;top:1988px;width:317px;height:293px;background:linear-gradient(135deg,#bdbdbd,#a39a94 45%,#2a3550)"></div>
    <div class="shot" role="img" aria-label="Woman in mustard blouse" style="left:585px;top:1988px;width:178px;height:142px;background:linear-gradient(#cfcfd1,#9a7a3a)"></div>
    <div class="shot" role="img" aria-label="Woman in black embroidered top" style="left:774px;top:1988px;width:171px;height:142px;background:linear-gradient(#d9d9db,#2b2b2e)"></div>
    <div class="shot" role="img" aria-label="Woman in checked shirt" style="left:585px;top:2140px;width:178px;height:141px;background:linear-gradient(#8f8f93,#d6cfcf)"></div>
    <div class="shot" role="img" aria-label="Woman in magenta blouse" style="left:774px;top:2140px;width:171px;height:141px;background:linear-gradient(#d8d8da,#8a1f3c)"></div>
  </section>
</main>

<footer>
  <div class="abs footer"></div>
  <div class="abs f-policy">ALL SALES FINAL. NO REFUNDS,<br>RETURNS OR EXCHANGES</div>
  <div class="abs f-rule"></div>
  <div class="abs f-contact">+xxx xxxx xxxxx<br>xxxxxxx@tavishirt.co</div>
  <div class="abs f-div" style="left:386px"></div>
  <div class="abs f-links"><div class="f-head">Contact Us</div><ul><li>Home</li><li>Collections</li><li>Shop Now</li><li>Contact</li></ul></div>
  <div class="abs f-div" style="left:616px"></div>
  <div class="abs f-news"><div class="f-head">Email Newsletter</div><p>Sale upto 20 % off for your next purchase inthis month!</p></div>
  <div class="abs subscribe"><div class="field">Email address</div><div class="btn">Subscribe</div></div>
  <div class="abs socials"><i></i><i></i><i></i><i></i><i></i></div>
  <div class="abs footer-bottom"></div>
  <div class="abs copy">© 2020 Tavi &nbsp;| All Rights Reserved</div>
  <div class="abs cards"><i></i><i></i><i></i><i></i><i></i><i></i></div>
</footer>

</body>
</html>
```